New Business Card Design Project

We are looking for a talented individual to create a truly awesome/unique business card design for us. We are looking for a someone to design something that will really stand out from the crowd - we don't mind what ideas you come up with (ie embossed/flat/matte/shine etc etc) just wow us with your creativity.
Updates

Target Market(s)

Video Games Industry Professionals (all levels of seniority from QA Testers through to CEOs)

Contact Information for Business Card

Company logo (see upload)
Company name: Northbay Play Careers Ltd
Employee Name: Darren Elsby
Job title: CEO
Website: www.nbpc2go.example
Office +44 1632 960418
Mobile: +44 7700 900276
Email: darren@nbpc2go.example

Colors

Designer to choose colors to be used in the design.

Requirements
Must have
• The business card design MUST contain all the information listed in the BUSINESS CARD DETAILS box.
• You will see the colours that are relevant to us (ie company logo) in the uploaded imagery - however you do not have to use all these colours when designing the business card itself
• MUST BE DOUBLE SIDED

```html
<!DOCTYPE html>
<html lang="en">
<head>
<meta charset="utf-8">
<title>Northbay Play Careers – Business Card</title>
<link rel="stylesheet" href="https://fonts.googleapis.com/css2?family=Russo+One&family=Crimson+Text:wght@400;600&display=swap">
<style>
  :root {
    --page-bg: #d4650f;
    --card-blue: #1d55e0;
    --card-blue-deep: #1238b8;
    --navy: #0b1a4a;
    --navy-soft: #10245e;
    --accent-orange: #ee7c12;
    --text-light: #ffffff;
  }
  html, body {
    margin: 0;
    padding: 0;
    width: 1200px;
    height: 1200px;
    overflow: hidden;
    background: var(--page-bg);
  }
  .canvas {
    width: 1200px;
    height: 1200px;
    display: flex;
    align-items: center;
    justify-content: center;
    gap: 32px;
  }
  .card {
    width: 552px;
    height: 314px;
    display: block;
    box-shadow: 0 6px 18px rgba(0,0,0,0.18);
  }
  .brand-name {
    font-family: "Russo One", sans-serif;
    fill: var(--text-light);
  }
  .person-name {
    font-family: "Russo One", sans-serif;
    fill: var(--text-light);
    font-size: 22px;
    letter-spacing: 0.5px;
  }
  .person-title {
    font-family: "Russo One", sans-serif;
    fill: var(--accent-orange);
    font-size: 6px;
    letter-spacing: 0.4px;
  }
  .contact-heading {
    font-family: "Crimson Text", serif;
    fill: var(--text-light);
    font-size: 11px;
  }
  .contact-web {
    font-family: "Russo One", sans-serif;
    fill: var(--text-light);
    font-size: 10px;
  }
  .contact-line {
    font-family: "Crimson Text", serif;
    fill: var(--text-light);
    font-size: 11.5px;
  }
  .icon {
    fill: none;
    stroke: var(--accent-orange);
    stroke-width: 1.4;
    stroke-linecap: round;
    stroke-linejoin: round;
  }
  .brand-dot { fill: var(--accent-orange); }
  .accent-stroke { fill: var(--accent-orange); }
  .panel { fill: var(--navy); }
</style>
</head>
<body>
<main class="canvas">

  <!-- Front side -->
  <svg class="card card-front" viewBox="0 0 460 262" xmlns="http://www.w3.org/2000/svg" aria-label="Business card front">
    <defs>
      <linearGradient id="front-blue" x1="0" y1="0" x2="1" y2="1">
        <stop offset="0" stop-color="var(--card-blue)"/>
        <stop offset="1" stop-color="var(--card-blue-deep)"/>
      </linearGradient>
      <radialGradient id="front-glow" cx="0.5" cy="0.5" r="0.6">
        <stop offset="0" stop-color="var(--navy-soft)"/>
        <stop offset="1" stop-color="var(--navy)"/>
      </radialGradient>
    </defs>
    <rect class="card-background" width="460" height="262" fill="url(#front-blue)" role="img" aria-label="Blue background with faint decorative pattern"/>
    <polygon class="accent-stroke frame-outer" points="84,0 282,0 424,131 282,262 84,262 38,131"/>
    <polygon class="panel frame-inner" points="92,0 276,0 412,131 276,262 92,262 50,131" fill="url(#front-glow)"/>
    <g class="brand-lockup">
      <circle class="brand-dot" cx="112" cy="133" r="20"/>
      <text class="brand-name" x="142" y="128" font-size="21">Northbay Play</text>
      <text class="brand-name" x="142" y="152" font-size="21">Careers</text>
    </g>
  </svg>

  <!-- Back side -->
  <svg class="card card-back" viewBox="0 0 460 262" xmlns="http://www.w3.org/2000/svg" aria-label="Business card back">
    <defs>
      <linearGradient id="back-blue" x1="0" y1="0" x2="1" y2="1">
        <stop offset="0" stop-color="var(--card-blue)"/>
        <stop offset="1" stop-color="var(--card-blue-deep)"/>
      </linearGradient>
    </defs>
    <rect class="card-background" width="460" height="262" fill="url(#back-blue)" role="img" aria-label="Blue background with faint decorative pattern"/>
    <polygon class="accent-stroke panel-edge" points="279,0 460,0 460,262 254,262 194,158 0,158 0,88 239,88"/>
    <polygon class="panel contact-panel" points="289,0 460,0 460,262 264,262 204,158 0,158 0,88 247,88"/>

    <g class="brand-lockup">
      <circle class="brand-dot" cx="36" cy="42" r="11"/>
      <text class="brand-name" x="53" y="40" font-size="11">Northbay Play</text>
      <text class="brand-name" x="53" y="53" font-size="11">Careers</text>
    </g>

    <g class="identity">
      <text class="person-name" x="30" y="125">DARREN ELSBY</text>
      <text class="person-title" x="42" y="142">• CHIEF EXECUTIVE OFFICER •</text>
    </g>

    <g class="contact-list">
      <text class="contact-heading" x="430" y="42" text-anchor="end">Contact us :</text>

      <g class="icon icon-web" transform="translate(310,80)">
        <circle cx="0" cy="0" r="7"/>
        <ellipse cx="0" cy="0" rx="3" ry="7"/>
        <line x1="-7" y1="0" x2="7" y2="0"/>
      </g>
      <text class="contact-web" x="325" y="84">WWW.NBPC2GO.EXAMPLE</text>

      <g class="icon icon-phone" transform="translate(310,126)">
        <path d="M-6,-7 L-3,-7 L-1,-3 L-3,-1 Q-1,3 3,5 L5,3 L8,5 L8,8 Q0,9 -5,2 Q-8,-3 -6,-7 Z"/>
      </g>
      <text class="contact-line" x="326" y="131">+44 1632 960418</text>

      <g class="icon icon-home" transform="translate(310,174)">
        <path d="M-7,0 L0,-7 L7,0 M-5,-2 L-5,7 L5,7 L5,-2 M-2,7 L-2,2 L2,2 L2,7"/>
      </g>
      <text class="contact-line" x="326" y="179">+44 7700 900276</text>

      <g class="icon icon-mail" transform="translate(310,222)">
        <rect x="-7" y="-5" width="14" height="10"/>
        <path d="M-7,-5 L0,1 L7,-5"/>
      </g>
      <text class="contact-line" x="324" y="226">darren@nbpc2go.example</text>
    </g>
  </svg>

</main>
</body>
</html>
```